Office Wall Poster plus other Wall Decal quotes in office

We have redesigned our office & require parts of our Culture statement to be displayed in our office. Our company is KOVA Estate Agents Group and our brand is all about being KOVA .. integrity, honesty, authenticity etc.
We have two areas we wish to decorate.
1. Reception
2. Meeting Room

RECEPTION
We want our leading culture statement to be displayed as large A0 size in a framed POSTER PRINT in our reception. The frame will be black.
WORDING: 'There's a reason we're called KOVA. KOVA is the essence of who we are'
Our brand colors are red, white, black. Our Red is CMYK 12,99, 92,02
When we type our name KOVA, we always use Venera font (always in caps). I have attached a file I personally created with 3 different ideas (I am not a designer) but we are not happy with any of them but it will give you an idea of what we are looking for. We want a simple statement so it stands out and not too busy.

MEETING ROOM
We have one black feature wall in this room and wish to dress this with a collection of quotes from our main Culture statement. We will have these printed as 'stick on wall decals' We have provided a collection of 8 quotes for you to design. Wording is to be in white colour with the key words to be METALLIC SILVER & in caps. We were planning to arrange them ad-hoc on the wall singularly, but if you have any creative ideas on how to display these, we are open to suggestions. Please provide your ideas on how best to arrange these on the black wall. Maybe even in a circle to represent our logo? But we truly do not have a clue - we are only real estate agents, not designers. That is why we would love suggetions on how best to make our Culture Statements work best.
Best of luck and we are excited to see your ideas!

Target Market(s)

Our clients need to get a great feel for what we are all about when they visit our office. Our culture needs to be seen and felt.

Industry/Entity Type

Real Estate

Font styles to use
Other font styles liked:
• We use Venera font when we type our name KOVA

Colors
EB3D1F
EC4F4E
F09395
F8D3D4
FCEDEE

Requirements
Should not have
• Not too busy, simple statements, easy to read

```html
<!DOCTYPE html>
<html lang="en">
<head>
<meta charset="utf-8">
<title>KOVA Culture Poster</title>
<link rel="stylesheet" href="https://fonts.googleapis.com/css2?family=Michroma&family=Allura&display=swap">
<style>
  :root {
    --backdrop: #bdbdbd;
    --ink-black: #0a0203;
    --deep-maroon: #3a0507;
    --brand-red: #e8141c;
    --poster-red: #b8141a;
    --white: #ffffff;
    --heart-tone: rgba(210, 40, 45, 0.18);
  }
  html, body {
    margin: 0;
    padding: 0;
    width: 1200px;
    height: 1200px;
    overflow: hidden;
    background: var(--backdrop);
  }
  .canvas {
    position: relative;
    width: 1200px;
    height: 1200px;
  }
  .poster {
    position: absolute;
    left: 207px;
    top: 68px;
    width: 786px;
    height: 1064px;
  }
  .sans { font-family: "Michroma", sans-serif; }
  .script { font-family: "Allura", cursive; }
  .lead-in { fill: var(--white); font-size: 21px; }
  .hero-name { fill: var(--white); font-size: 142px; }
  .called { fill: var(--brand-red); font-size: 92px; }
  .closing-name { fill: var(--brand-red); font-size: 74px; }
  .essence { fill: var(--white); font-size: 64px; }
  .group-name { fill: var(--white); font-size: 14px; }
</style>
</head>
<body>
<main class="canvas">
  <svg class="poster" viewBox="0 0 786 1064" xmlns="http://www.w3.org/2000/svg" role="group" aria-label="There's a reason we're called KOVA. KOVA is the essence of who we are">
    <defs>
      <linearGradient id="poster-bg" x1="0" y1="0" x2="0" y2="1">
        <stop offset="0" stop-color="var(--ink-black)"/>
        <stop offset="0.35" stop-color="var(--deep-maroon)"/>
        <stop offset="1" stop-color="var(--poster-red)"/>
      </linearGradient>
      <radialGradient id="heart-glow" cx="0.5" cy="0.5" r="0.5">
        <stop offset="0" stop-color="var(--heart-tone)"/>
        <stop offset="1" stop-color="rgba(210,40,45,0)"/>
      </radialGradient>
    </defs>

    <rect class="poster-background" width="786" height="1064" fill="url(#poster-bg)" role="img" aria-label="Dark textured wood background fading from black to red"/>

    <rect class="heart-motif" x="166" y="360" width="510" height="380" rx="190" fill="url(#heart-glow)" role="img" aria-label="Faint pair of interlocking outlined hearts"/>

    <text class="lead-in sans" x="77" y="81" textLength="296" lengthAdjust="spacingAndGlyphs">THERE'S A REASON</text>
    <text class="hero-name sans" x="77" y="238" textLength="574" lengthAdjust="spacingAndGlyphs">KOVA</text>
    <text class="called script" x="86" y="140" textLength="426" lengthAdjust="spacingAndGlyphs">we're called</text>

    <text class="closing-name sans" x="324" y="933" textLength="412" lengthAdjust="spacingAndGlyphs">KOVA</text>
    <text class="essence script" x="321" y="982" textLength="413" lengthAdjust="spacingAndGlyphs">is the essence of</text>
    <text class="essence script" x="388" y="1036" textLength="281" lengthAdjust="spacingAndGlyphs">who we are</text>

    <g class="group-name-block">
      <text class="group-name sans" x="150" y="905" text-anchor="middle">KOVA Estate</text>
      <text class="group-name sans" x="150" y="927" text-anchor="middle">Agents Group</text>
    </g>
  </svg>
</main>
</body>
</html>
```